Corbel Crest Lighting - Commercial & Residential Landscape Lighting

Landscape Lighting Services & Design: Create a website for our landscape lighting company. We would like the design to be tailored around this description:
Illuminate with Confidence. Designed with Precision. Installed with Care.
Locally and veteran-owned, we take pride in transforming outdoor spaces through innovative lighting solutions tailored to your vision. From landscape and holiday lighting to permanent installations, our effortless process and expert design deliver breathtaking results and lasting curb appeal. Backed by a lifetime warranty and quarterly service options, our commitment to quality and customer satisfaction is unwavering. Try before you buy and experience your home in a whole new light with our complimentary demo kit — see the stunning effects before you decide.
- Also, add in this information as well; Outdoor Lighting not only beautifies spaces but also significantly enhances safety by illuminating your home or business. Beautifully lit entrances deter potential intruders, making your home a safer place for your loved ones. we also offer quarterly service plans to ensure lighting equipment continues to operate & illuminate effectively throughout the year. Also mention we provide free estimates and we are offering a 10% discount to military, veterans, and first responders.

Target Market(s)

Luxury market

Industry/Entity Type

Landscape Lighting - Residential & Commercial Lighting Services

Coding

Coded - Design and coding required

Number of Pages Required

2 page

Colors
00AB8E
00BBA5
67D7C9
C6EFE9
E9F9F6
59FF00
82FF00
B8FF75
E3FFCB
F4FFEA
FFC000
F8CF3A
FAE287
FDF2CF
FEFAEE

Requirements
Must have
• a lead generation button where people can submit their information for us to reach out to them and schedule their free estimate, homepage, about page, contact page, products and services page, user friendly, easy to navigate, and it also must be engaging and eye popping, as well as appealing to the luxury market. Please use colors; verdent green, dark green, ivory, and sunny yellow. Also, include an about page that references our story; Glen is retired Army and he opened a fitness studio in 2017 with his wife Rosalind. He has installed low voltage lighting in every home he lived in and for his friends and family over the years and decided to open his own business because he is passionate about beautifying outdoor landscapes and highlighting a properties full potential, not only in the day but at night as well all while providing safety and security for his clients. Having a deep respect for nature and landscaping, he wants to provide the same care and quality to each of his clients as he has in the fitness industry for decades. He believes small businesses are the back bone of America and he's excited to provide a service that is all to often neglected in the design of a home.
Nice to have
• I would like to have a clear intent and purpose, engaging web design, clear call to action, optimized for search engines, mobile friendy design, security measures, credibility indicators

```html
<!DOCTYPE html>
<html lang="en">
<head>
<meta charset="utf-8">
<title>Corbel Crest Lighting – Commercial &amp; Residential Landscape Lighting</title>
<link rel="stylesheet" href="https://fonts.googleapis.com/css2?family=Archivo:wdth,wght@62..125,300..700&family=Poppins:wght@300;400;500&display=swap">
<style>
:root{
  --ink:#0b0b0b;
  --ivory:#ffffff;
  --sun:#fcc40a;
  --sun-bright:#fff44f;
  --forest:#3a5410;
  --verdant:#1f6b3a;
  --espresso:#1e120a;
  --bar:#2d2d2d;
  --muted:#7a7a7a;
  --field:#f4f4f4;
}
*{box-sizing:border-box;margin:0;padding:0}
html,body{width:1200px;height:4914px;overflow:hidden}
body{position:relative;background:var(--ivory);color:var(--ink);font-family:"Poppins",sans-serif}
.abs{position:absolute}
.display{font-family:"Archivo",sans-serif;font-stretch:118%;font-weight:400;letter-spacing:-0.02em;line-height:1;white-space:nowrap}

/* header */
.site-header{left:0;top:0;width:1200px;height:86px;background:var(--ink)}
.brand{font-family:"Archivo",sans-serif;font-stretch:110%;color:var(--sun);font-weight:500;font-size:17px;letter-spacing:.06em;line-height:1.1;white-space:nowrap}
.brand small{display:block;font-size:8px;letter-spacing:.18em}
.nav a{position:absolute;top:34px;color:#fff;font-size:13px;text-decoration:none;white-space:nowrap}
.cta-pill{left:927px;top:29px;width:189px;height:32px;border-radius:16px;background:#fff;color:var(--ink);font-size:12.5px;display:flex;align-items:center;justify-content:center}

/* hero */
.hero-photo{left:0;top:86px;width:1200px;height:576px;background:linear-gradient(160deg,#12203f 0%,#1b2a4a 35%,#5b4a3a 60%,#2d3820 85%,#3b2a1d 100%)}
.hero-card{left:0;top:244px;width:378px;height:439px;background:var(--ink);color:#fff}
.hero-title{left:42px;top:72px;font-family:"Archivo",sans-serif;font-stretch:112%;font-weight:300;font-size:50px;line-height:62px;letter-spacing:-.01em}
.hero-tag{left:95px;top:269px;width:233px;height:31px;background:var(--sun-bright);transform:skewX(-16deg)}
.hero-tag span{display:block;transform:skewX(16deg);color:var(--ink);font-size:15px;text-align:center;line-height:31px;white-space:nowrap}
.hero-care{left:40px;top:312px;font-family:"Archivo",sans-serif;font-stretch:112%;font-weight:300;font-size:31px;color:var(--sun-bright);white-space:nowrap}
.hero-dots{left:1059px;top:605px}

/* intro */
.intro-1{left:-4px;top:782px;font-size:132px}
.intro-2{left:270px;top:928px;font-size:130px}
.intro-sub{left:277px;top:1056px;font-family:"Archivo",sans-serif;font-stretch:105%;font-size:52px;line-height:1;white-space:nowrap}
.intro-copy{left:279px;top:1131px;width:612px;font-size:10.5px;line-height:14.5px;color:#333}
.btn-dark{background:var(--ink);color:#fff;border-radius:14px;display:flex;align-items:center;justify-content:center;font-size:10.5px;white-space:nowrap}

/* service rows */
.svc-title{font-family:"Archivo",sans-serif;font-stretch:105%;font-size:28px;line-height:33px;white-space:nowrap}
.svc-copy{font-size:10.5px;line-height:16px;color:var(--muted)}
.read-more{font-size:11px;color:var(--verdant);display:flex;align-items:center;gap:10px;white-space:nowrap}
.read-more i{display:block;width:36px;height:4px;background:var(--verdant)}
.photo-office{left:0;top:1313px;width:658px;height:360px;background:linear-gradient(135deg,#f2f2f0,#d9d7d2 55%,#8a8b86)}
.photo-trees{left:0;top:1723px;width:1200px;height:439px;background:linear-gradient(120deg,#20361a,#3b4a1c 40%,#1a2a14 70%,#0e1a0e)}
.safety-box{left:0;top:1862px;width:477px;height:300px;background:var(--forest);color:#fff}
.photo-lounge{left:538px;top:2236px;width:662px;height:372px;background:radial-gradient(circle at 45% 35%,#c07b36 0%,#6a3a18 35%,#2a150a 75%)}

/* products */
.products{left:0;top:2652px;width:1200px;height:549px;background:var(--sun)}
.products-title{left:-4px;top:-28px;font-size:112px;color:#fff}
.card{width:248px;height:275px;background:#fff;border-radius:4px;top:160px}
.card .shot{position:absolute;left:44px;top:20px;width:160px;height:200px;border-radius:4px;background:linear-gradient(180deg,#e9e9e9,#9a9a9a)}
.card p{position:absolute;left:0;right:0;top:243px;text-align:center;font-size:11.5px;white-space:nowrap}
.view-bar{left:0;top:3201px;width:1200px;height:52px;background:var(--bar);color:#fff;font-size:14px;display:flex;align-items:center;justify-content:center;gap:12px}

/* demo */
.demo-rule{left:222px;top:3291px;width:3px;height:200px;background:var(--ink)}
.demo-copy{left:256px;top:3316px;width:680px;font-family:"Archivo",sans-serif;font-stretch:108%;font-size:35px;line-height:40px;color:#222}
.photo-facade{left:391px;top:3648px;width:588px;height:334px;background:linear-gradient(120deg,#0d0a08,#3a2a1a 50%,#0a0806)}
.photo-installer{left:34px;top:3591px;width:558px;height:391px;background:linear-gradient(160deg,#e0e0e0,#a8a8a8)}
.service-box{left:801px;top:3734px;width:363px;height:187px;background:var(--espresso);color:#fff;font-size:14px;line-height:20px;padding:48px 34px 0 36px}

/* estimate */
.upgrade-1{left:-4px;top:4118px;font-size:86px}
.upgrade-2{left:353px;top:4203px;font-size:86px}
.estimate-side{left:198px;top:4327px;width:6px;height:234px;background:var(--sun-bright)}
.estimate-label{left:82px;top:4430px;width:200px;transform:rotate(-90deg);font-size:17px;text-align:center;white-space:nowrap}
.field-label{font-size:10px;color:#444;white-space:nowrap}
.field{height:30px;border:1px solid #d8d8d8;border-radius:12px;background:var(--field)}
.ticker-rule{left:0;top:4602px;width:1200px;height:1px;background:#ccc}
.ticker{left:10px;top:4614px;white-space:nowrap;font-family:"Archivo",sans-serif;font-stretch:108%;font-weight:300;font-size:30px}

/* footer */
.site-footer{left:0;top:4665px;width:1200px;height:249px;background:var(--ink);border-radius:70px 70px 0 0;color:#fff}
.foot-links a{display:block;color:#fff;text-decoration:none;font-size:10px;line-height:21px}
.foot-head{font-size:13px;white-space:nowrap}
.foot-item{font-size:11px;display:flex;align-items:center;gap:7px;white-space:nowrap}
.social{display:flex;gap:10px}
.social i{display:block;width:9px;height:9px;border-radius:50%;background:#fff}
.copyright{left:715px;top:216px;font-size:9.5px;color:#bbb;white-space:nowrap}
</style>
</head>
<body>

<header class="site-header abs">
  <div class="brand abs" style="left:102px;top:24px">CORBEL CREST<small>SIGNATURE LIGHTING</small></div>
  <nav class="nav">
    <a style="left:452px">Home</a>
    <a style="left:522px">About</a>
    <a style="left:594px">Products</a>
    <a style="left:683px">Services</a>
    <a style="left:768px">Contact Us</a>
  </nav>
  <div class="cta-pill abs">Schedule a free estimate</div>
</header>

<section class="hero">
  <div class="hero-photo abs" role="img" aria-label="Two-storey house with landscape lighting at dusk"></div>
  <svg class="hero-dots abs" width="141" height="57" viewBox="0 0 141 57">
    <polygon points="30,0 141,0 141,57 0,57" fill="var(--sun-bright)"/>
    <circle cx="82" cy="28" r="5" fill="#111"/><circle cx="94" cy="28" r="5" fill="#111"/>
    <circle cx="106" cy="28" r="4.5" fill="none" stroke="#111" stroke-width="1.2"/>
  </svg>
  <div class="hero-card abs">
    <h1 class="hero-title abs">Illuminate<br>with<br>Confidence.</h1>
    <div class="hero-tag abs"><span>Designed with Precision</span></div>
    <div class="hero-care abs">Installed with Care.</div>
  </div>
</section>

<section class="intro">
  <div class="intro-1 display abs">COMMERCIAL</div>
  <div class="intro-2 display abs">&amp; RESIDENTIAL</div>
  <h2 class="intro-sub abs" style="font-weight:400">Landscape Lighting</h2>
  <p class="intro-copy abs">Locally and veteran-owned, we take pride in transforming outdoor spaces through innovative lighting solutions tailored to your vision. From landscape and holiday lighting to permanent installations, our effortless process and expert design deliver breathtaking results and lasting curb appeal. Backed by a lifetime warranty and quarterly service options, our commitment to quality and customer satisfaction is unwavering.</p>
  <div class="btn-dark abs" style="left:280px;top:1210px;width:115px;height:27px">Contact us</div>
</section>

<section class="service-commercial">
  <div class="photo-office abs" role="img" aria-label="Bright office interior with linear ceiling lights"></div>
  <h3 class="svc-title abs" style="left:700px;top:1343px;font-weight:400">Commercial<br>Landscape Lighting</h3>
  <p class="svc-copy abs" style="left:700px;top:1444px;width:250px">Outdoor Lighting not only beautifies spaces but also significantly enhances safety by illuminating your home or business. Beautifully lit entrances deter potential intruders, making your home a safer place for your loved ones. we also offer quarterly service plans to ensure lighting equipment continues to operate &amp; illuminate effectively throughout the year.</p>
  <div class="read-more abs" style="left:701px;top:1612px">Read more <i></i></div>
</section>

<section class="safety">
  <div class="photo-trees abs" role="img" aria-label="Garden trees with hanging lanterns glowing at night"></div>
  <div class="safety-box abs">
    <p class="abs" style="left:53px;top:55px;width:390px;font-size:20px;line-height:23px">Outdoor Lighting not only beautifies spaces but also significantly enhances safety by illuminating your home or business.</p>
    <div class="abs" style="left:202px;top:178px;width:2px;height:122px;background:#fff"></div>
    <p class="abs" style="left:229px;top:194px;width:210px;font-size:10.5px;line-height:15px">Beautifully light entrances deter potential intruders, making your home a safer place for your loved ones.</p>
  </div>
</section>

<section class="service-residential">
  <h3 class="svc-title abs" style="left:238px;top:2280px;font-weight:400">Residential<br>Landscape Lighting</h3>
  <p class="svc-copy abs" style="left:238px;top:2364px;width:250px">Outdoor Lighting not only beautifies spaces but also significantly enhances safety by illuminating your home or business. Beautifully lit entrances deter potential intruders, making your home a safer place for your loved ones. we also offer quarterly service plans to ensure lighting equipment continues to operate &amp; illuminate effectively throughout the year.</p>
  <div class="read-more abs" style="left:239px;top:2539px">Read more <i></i></div>
  <div class="photo-lounge abs" role="img" aria-label="Living room with warm woven pendant lights"></div>
</section>

<section class="products abs">
  <h2 class="products-title display abs">Featured Products</h2>
  <svg class="abs" style="left:1027px;top:92px" width="106" height="46" viewBox="0 0 106 46">
    <circle cx="23" cy="23" r="22" fill="#fbe08a"/><circle cx="83" cy="23" r="22" fill="#fbe08a"/>
    <path d="M27 15 L19 23 L27 31" fill="none" stroke="#111" stroke-width="2"/>
    <path d="M79 15 L87 23 L79 31" fill="none" stroke="#111" stroke-width="2"/>
  </svg>
  <div class="card abs" style="left:78px"><div class="shot" role="img" aria-label="Linear floodlight fixture"></div><p>Linear Floodlight</p></div>
  <div class="card abs" style="left:347px"><div class="shot" role="img" aria-label="Suspended blade pendant fixture"></div><p>Slimline Blade Pendant</p></div>
  <div class="card abs" style="left:620px"><div class="shot" role="img" aria-label="Round spotlight on a post"></div><p>Orbit Spot</p></div>
  <div class="card abs" style="left:887px"><div class="shot" role="img" aria-label="Multi-head spotlight pole"></div><p>Orbit Spot</p></div>
</section>
<div class="view-bar abs">View our products
  <svg width="48" height="10" viewBox="0 0 48 10"><path d="M0 5 H46 M41 1 L46 5 L41 9" fill="none" stroke="#fff" stroke-width="1.2"/></svg>
</div>

<section class="demo">
  <div class="demo-rule abs"></div>
  <p class="demo-copy abs">Try before you buy and experience your home in a whole new light with our complimentary demo kit — see the stunning effects before you decide.</p>
  <div class="photo-facade abs" role="img" aria-label="Modern building facade lit at night" style="clip-path:polygon(30% 0,100% 0,100% 100%,0 100%,0 52%)"></div>
  <div class="photo-installer abs" role="img" aria-label="Electrician installing a ceiling light" style="clip-path:polygon(0 0,100% 0,50% 100%,48% 100%)"></div>
  <div class="service-box abs">We also offer quarterly service plans to ensure lighting equipment continues to operate &amp; illuminate effectively throughout the year.</div>
</section>

<section class="estimate">
  <div class="upgrade-1 display abs">UPGARDE YOUR INDOOR</div>
  <div class="upgrade-2 display abs">&amp; OUTDOOR TODAY.</div>
  <div class="estimate-side abs"></div>
  <div class="estimate-label abs">Schedule a free estimate</div>
  <span class="field-label abs" style="left:250px;top:4368px">Name</span>
  <div class="field abs" style="left:238px;top:4388px;width:235px"></div>
  <span class="field-label abs" style="left:498px;top:4366px">Email</span>
  <div class="field abs" style="left:481px;top:4388px;width:232px"></div>
  <span class="field-label abs" style="left:738px;top:4381px">Phone</span>
  <div class="field abs" style="left:721px;top:4400px;width:233px"></div>
  <div class="field abs" style="left:238px;top:4438px;width:718px;height:74px"><span class="field-label abs" style="left:15px;top:10px">Your Message</span></div>
  <div class="btn-dark abs" style="left:521px;top:4525px;width:131px;height:29px">Submit Query</div>
  <div class="ticker-rule abs"></div>
  <p class="ticker abs">we provide free estimates and we are offering a 10% discount to military, veterans, and first</p>
</section>

<footer class="site-footer abs">
  <div class="brand abs" style="left:240px;top:78px">CORBEL CREST<small>SIGNATURE LIGHTING</small></div>
  <nav class="foot-links abs" style="left:425px;top:56px">
    <a>Home</a><a>About Us</a><a>Services</a><a>Products</a><a>Contact Us</a>
  </nav>
  <div class="foot-head abs" style="left:548px;top:55px">Contact Us</div>
  <div class="foot-item abs" style="left:550px;top:85px">
    <svg width="10" height="10" viewBox="0 0 24 24"><path d="M6 2 L10 2 L11 7 L8 9 C9.5 12 12 14.5 15 16 L17 13 L22 14 L22 18 C22 20 20 22 18 22 C9 21 3 15 2 6 C2 4 4 2 6 2Z" fill="#fff"/></svg>(555) 014-2290</div>
  <div class="foot-item abs" style="left:550px;top:108px">
    <svg width="10" height="8" viewBox="0 0 20 16"><rect x="1" y="1" width="18" height="14" fill="none" stroke="#fff" stroke-width="2"/><path d="M1 1 L10 9 L19 1" fill="none" stroke="#fff" stroke-width="2"/></svg>support@corbelcrest.com</div>
  <div class="foot-head abs" style="left:771px;top:55px">Follow Us</div>
  <div class="social abs" style="left:773px;top:85px"><i></i><i></i><i></i><i></i><i></i></div>
  <p class="copyright abs">©2025 Corbel Crest Lighting. All Rights Reserved.</p>
</footer>

</body>
</html>
```